Quarrow - Business Card Design

Design a modern masculine business card for our business

Target Market(s)

Private Market

Industry/Entity Type

Construction

Contact Information for Business Card

Company Name - Name of Person - Address - email address - contact number

Font styles to use
Serif
Sans Serif

Colors
0094D4
00A9DD
6FCCEA
C7EBF8
E9F6FB
00AB8E
00BBA5
67D7C9
C6EFE9
E9F9F6
F0912C
F2A743
F7CA91
FBE8D2
FDF5EE

Requirements
Must have
• Use company logo provided
Nice to have
• Company Logo

```html
<!DOCTYPE html>
<html lang="en">
<head>
<meta charset="utf-8">
<title>Quarrow - Business Card Design</title>
<link href="https://fonts.googleapis.com/css2?family=Arimo:ital,wght@0,400;0,700;1,400&display=swap" rel="stylesheet">
<style>
  :root {
    --backdrop: #3b3633;
    --card: #f4f4f6;
    --orange: #e36826;
    --ink: #111111;
    --white: #ffffff;
    --shadow: rgba(0, 0, 0, 0.45);
  }
  * { margin: 0; padding: 0; box-sizing: border-box; }
  html, body {
    width: 1200px;
    height: 716px;
    overflow: hidden;
    background: var(--backdrop);
    font-family: "Arimo", Arial, sans-serif;
  }
  .canvas {
    position: relative;
    width: 1200px;
    height: 716px;
  }
  .card {
    position: absolute;
    top: 209px;
    width: 520px;
    height: 298px;
    background: var(--card);
    box-shadow: 0 10px 28px var(--shadow);
    overflow: hidden;
  }
  .card--front { left: 50px; }
  .card--back { left: 630px; }

  .card__shapes {
    position: absolute;
    inset: 0;
    width: 100%;
    height: 100%;
  }
  .shape-band { fill: var(--orange); }
  .shape-corner { fill: var(--ink); }

  .contact {
    position: absolute;
    left: 26px;
    color: var(--white);
    font-style: italic;
    font-size: 11.5px;
    line-height: 1.35;
  }
  .contact--phone { top: 64px; }
  .contact--address { top: 160px; }

  .person {
    position: absolute;
    right: 96px;
    top: 78px;
    text-align: right;
  }
  .person__name {
    font-weight: 700;
    font-size: 17px;
    color: var(--ink);
    line-height: 1.1;
  }
  .person__role {
    font-weight: 700;
    font-size: 12.5px;
    color: var(--orange);
    line-height: 1.2;
  }
  .person__email {
    margin-top: 6px;
    font-size: 11.5px;
    color: var(--ink);
  }

  .brand {
    position: absolute;
    display: flex;
    align-items: center;
    gap: 8px;
    font-weight: 700;
    color: var(--ink);
    white-space: nowrap;
  }
  .brand__square {
    display: block;
    background: var(--orange);
  }
  .brand--small {
    left: 212px;
    top: 226px;
    font-size: 17px;
  }
  .brand--small .brand__square { width: 14px; height: 14px; }
  .brand--large {
    left: 50%;
    top: 50%;
    transform: translate(-50%, -50%);
    font-size: 32px;
    gap: 14px;
  }
  .brand--large .brand__square { width: 28px; height: 28px; }
</style>
</head>
<body>
<main class="canvas">
  <section class="card card--front" aria-label="Business card front">
    <svg class="card__shapes" viewBox="0 0 520 298" preserveAspectRatio="none" aria-hidden="true">
      <polygon class="shape-band" points="0,0 182,0 158,298 0,298"/>
      <polygon class="shape-corner" points="438,0 520,0 438,150"/>
    </svg>
    <p class="contact contact--phone">(555) 0142-7781</p>
    <p class="contact contact--address">2719 Hollister Avenue<br>Cedar Ridge, NY 11920</p>
    <div class="person">
      <p class="person__name">Marcus Hale</p>
      <p class="person__role">President</p>
      <p class="person__email">info@quarrowbuild.com</p>
    </div>
    <div class="brand brand--small">
      <span class="brand__square" aria-hidden="true"></span>
      <span class="brand__name">Quarrow Construction, Inc</span>
    </div>
  </section>

  <section class="card card--back" aria-label="Business card back">
    <div class="brand brand--large">
      <span class="brand__square" aria-hidden="true"></span>
      <span class="brand__name">Quarrow Construction, Inc</span>
    </div>
  </section>
</main>
</body>
</html>
```